Business Card Design Project

I am a property development company requiring a professional looking business card.
The name of the my company is PLW CANOPIES. I have attached a couple of designs that I have created on my own, that can give you an idea of what I am after.
Above the wording PLW CANOPIES, I have a orange arc above these words to signify the sun is begining to rise above the horizon.
I have a few designs; Middle Rays, Side Rays, Horizontals Rays which are OK, but I am looking for the better design.
The Rear design of the card is what I had came up with. If you have a better design, I am happy to see it.
The design of the card can follow what I have came up with, or it can be totally different. The fonts needs to be adjusted to another font that is more suitable.
The colours that I have used is what I think I would like to stick with. As I have mentioned, the orange arc is to signify the sun rising. If you have a better colour scheme, I would consider it.
Looking at dealing with first home buyers and proffesional people.
Business

```html
<!DOCTYPE html>
<html lang="en">
<head>
<meta charset="utf-8">
<title>PLW Canopies – Business Card</title>
<link href="https://fonts.googleapis.com/css2?family=Arimo:ital,wght@0,400;0,700;1,400&family=Questrial&display=swap" rel="stylesheet">
<style>
  :root {
    --page: #ffffff;
    --card-black: #000000;
    --card-grey: #d3d1ce;
    --label: #111111;
    --white: #ffffff;
    --text-dark: #1a1a1a;
    --text-mid: #505050;
    --tagline: #8a8a8a;
    --rule: #8c8c8c;
    --orange-deep: #d9731a;
    --orange: #f0a22e;
    --sun-cream: #fbe6b8;
  }
  * { margin: 0; padding: 0; box-sizing: border-box; }
  html, body { width: 900px; height: 1200px; overflow: hidden; background: var(--page); }
  .canvas { position: relative; width: 900px; height: 1200px; }

  .side-label {
    position: absolute; left: 213px;
    font-family: "Arimo", Arial, sans-serif; font-size: 19px; color: var(--label);
  }
  .side-label--back { top: 229px; }
  .side-label--front { top: 644px; }

  .card { position: absolute; width: 493px; overflow: hidden; }

  /* Back of card */
  .card--back { left: 211px; top: 265px; height: 289px; background: var(--card-grey); border: 1px solid #6d6d6d; }
  .back-top {
    position: absolute; left: 0; top: 0; width: 100%; height: 127px; background: var(--card-black);
  }
  .holder-name {
    position: absolute; left: 0; width: 100%; top: 78px; text-align: center;
    font-family: "Arimo", Arial, sans-serif; font-weight: 700; font-size: 19px; color: var(--white);
  }
  .holder-role {
    position: absolute; left: 0; width: 100%; top: 101px; text-align: center;
    font-family: "Arimo", Arial, sans-serif; font-style: italic; font-size: 15px; color: var(--white);
  }
  .horizon-band {
    position: absolute; left: 0; top: 127px; width: 100%; height: 30px;
    background: linear-gradient(to bottom, var(--orange-deep), var(--orange) 40%, var(--sun-cream));
  }
  .contact { position: absolute; left: 0; top: 170px; width: 100%; text-align: center; }
  .brand-name {
    display: inline-flex; align-items: center; gap: 6px;
    font-family: "Questrial", "Century Gothic", sans-serif; font-size: 21px; line-height: 22px; color: var(--text-mid);
  }
  .brand-dot { width: 9px; height: 9px; border-radius: 50%; background: var(--orange); }
  .contact-address {
    font-family: "Arimo", Arial, sans-serif; font-weight: 700; font-size: 13.5px; letter-spacing: 0.4px;
    line-height: 17px; color: var(--text-dark);
  }
  .contact-line {
    font-family: "Questrial", "Century Gothic", sans-serif; font-size: 14.5px; line-height: 17px; color: var(--text-mid);
  }

  /* Front of card */
  .card--front { left: 213px; top: 684px; height: 287px; background: var(--card-black); }
  .front-brand {
    position: absolute; left: 0; width: 100%; top: 186px; text-align: center;
  }
  .front-brand .brand-name { font-size: 31px; line-height: 34px; color: var(--white); gap: 10px; }
  .front-brand .brand-dot { width: 12px; height: 12px; }
  .front-rule { position: absolute; left: 0; top: 222px; width: 100%; height: 2px; background: var(--rule); }
  .tagline {
    position: absolute; left: 0; width: 100%; top: 226px; text-align: center;
    font-family: "Questrial", "Century Gothic", sans-serif; font-size: 14px; letter-spacing: 9px; color: var(--tagline);
  }
</style>
</head>
<body>
<div class="canvas">
  <div class="side-label side-label--back">back</div>
  <section class="card card--back">
    <div class="back-top">
      <div class="holder-name">Martin Lowe</div>
      <div class="holder-role">Director</div>
    </div>
    <div class="horizon-band" role="img" aria-label="Decorative sunrise horizon band in orange to cream"></div>
    <div class="contact">
      <div class="brand-name"><span class="brand-dot"></span>plwcanopies</div>
      <div class="contact-address">48 Keel Street Ashby NSW 2190 Australia</div>
      <div class="contact-line">0412 308 954</div>
      <div class="contact-line">martin@plwcanopies.com.au</div>
      <div class="contact-line">www.plwcanopies.com.au</div>
    </div>
  </section>

  <div class="side-label side-label--front">front</div>
  <section class="card card--front">
    <div class="front-brand">
      <div class="brand-name"><span class="brand-dot"></span>plwcanopies</div>
    </div>
    <div class="front-rule"></div>
    <div class="tagline">property developments</div>
  </section>
</div>
</body>
</html>
```